HANDYMAN SERVICES

we provide a good,and reliable service.we do all aspects of home improvement ,also all garden services,and any repairs,no job too small,free quotes .
I am aiming towards the general public for clients,also be doing special rates for the elderly,and reducing the price for anyone who does a friend reference. It will be free quotes/consultation,all work will be guaranteed.
Now the type of work we do is cctv installation,decking,patio/driveway cleaning,garages for erecting/repairs,house/garage clearances,fit alarm systems,fit or repair windows/doors,lay patios,repair roofs,decorate interior/external,erect ariaels,lay driveways,erect or repair fencing,lay drainage,repair or erect guttering and soffits,water features,erect or repair kitchens/bathrooms,also plastering,lay lawns or repair,also repair/erect sheds.

```html
<!DOCTYPE html>
<html lang="en">
<head>
<meta charset="utf-8">
<title>Handyman Services</title>
<link href="https://fonts.googleapis.com/css2?family=Arimo:wght@400;700&display=swap" rel="stylesheet">
<style>
  :root {
    --paper: #ffffff;
    --roof-line: #d6d6d6;
    --tile: #ededed;
    --tile-edge: #ffffff;
    --tile-shadow: rgba(0,0,0,0.18);
    --ink: #2b2b2b;
    --icon: #6a6a6a;
    --banner: #f3e9a9;
    --badge: #f6e24a;
    --grass: #2e9a3a;
    --grass-light: #8fcf6a;
    --white: #ffffff;
  }
  * { box-sizing: border-box; margin: 0; padding: 0; }
  html, body { width: 1200px; height: 852px; overflow: hidden; background: var(--paper); }
  body { font-family: "Arimo", Arial, sans-serif; color: var(--ink); }
  .flyer { position: relative; width: 1200px; height: 852px; overflow: hidden; background: var(--paper); }

  .house { position: absolute; left: 0; top: 0; }

  .banner { position: absolute; left: 0; top: 60px; width: 460px; height: 66px;
    background: var(--banner); clip-path: polygon(0 0, 100% 0, 88% 100%, 0 100%); }
  .brand { position: absolute; left: 110px; top: 66px; font-weight: 700; font-size: 25px; line-height: 29px; color: #111; }
  .tool-mark { position: absolute; left: 56px; top: 40px; width: 62px; height: 170px;
    background: linear-gradient(#8a8a8a, #5d5d5d); border-radius: 14px; }

  .intro { position: absolute; left: 300px; top: 132px; width: 600px; text-align: center; font-weight: 700; color: #111; }
  .intro h1 { font-size: 26px; line-height: 32px; margin-bottom: 4px; }
  .intro p { font-size: 18.5px; line-height: 24px; }

  .roofer { position: absolute; left: 878px; top: 8px; width: 104px; height: 146px;
    background: linear-gradient(#9a9a9a, #6c6c6c); border-radius: 6px; }
  .roof-label { position: absolute; left: 992px; top: 118px; font-size: 19px; }

  .tile { position: absolute; background: var(--tile); border: 3px solid var(--tile-edge);
    box-shadow: 0 2px 5px var(--tile-shadow); display: flex; align-items: center; gap: 14px; padding: 0 10px 0 14px; }
  .tile .icon { flex: 0 0 62px; height: 52px; background: var(--icon); border-radius: 4px; opacity: .85; }
  .tile .label { font-size: 18.5px; line-height: 22px; }
  .tile.tall .icon { height: 70px; }

  .c1 { left: 130px; width: 270px; }
  .c2 { left: 414px; width: 272px; }
  .c3 { left: 700px; width: 274px; }
  .r1 { top: 254px; height: 126px; }
  .r2 { top: 396px; height: 128px; }
  .r3 { top: 540px; height: 64px; }
  .r4 { top: 620px; height: 72px; }
  .split { flex-direction: column; align-items: stretch; justify-content: center; gap: 0; padding: 0; }
  .split .part { display: flex; align-items: center; gap: 14px; padding: 0 10px 0 14px; }
  .split .part + .part { border-top: 2px solid #c9c9c9; margin: 0 10px 0 90px; padding: 6px 0 0 0; }
  .split .part .icon { flex: 0 0 62px; height: 60px; background: var(--icon); border-radius: 4px; opacity: .85; }

  .badge { position: absolute; left: 950px; top: 306px; width: 250px; height: 250px; }
  .badge-text { position: absolute; left: 992px; top: 372px; width: 166px; text-align: center;
    font-weight: 700; font-size: 17.5px; line-height: 21px; color: #222; }
  .badge-text hr { border: 0; border-top: 2px solid #6b5f14; margin: 6px 4px; }

  .lawn { position: absolute; left: 0; top: 700px; width: 1200px; height: 92px;
    background: linear-gradient(to bottom, rgba(143,207,106,0), var(--grass-light)); }
  .mower { position: absolute; left: 924px; top: 632px; width: 164px; height: 146px;
    background: linear-gradient(#3a3a3a, #111);
    clip-path: polygon(60% 0, 100% 0, 100% 100%, 0 100%, 0 68%, 60% 68%); }
  .lawn-label { position: absolute; left: 800px; top: 740px; font-size: 19px; }
  .ground { position: absolute; left: 0; top: 786px; width: 1200px; height: 40px; background: var(--grass); }
  .ground::before { content: ""; position: absolute; left: 0; right: 0; top: 18px;
    border-top: 3px dashed var(--white); }
  .ground-label { position: absolute; left: 636px; top: 7px; padding: 0 10px; background: var(--grass);
    color: var(--white); font-size: 19px; line-height: 24px; }
</style>
</head>
<body>
<main class="flyer">
  <svg class="house" width="1200" height="852" viewBox="0 0 1200 852" aria-hidden="true">
    <polyline points="62,278 600,22 1136,278" fill="none" stroke="var(--roof-line)" stroke-width="14" stroke-linejoin="miter"/>
    <line x1="116" y1="252" x2="116" y2="710" stroke="var(--roof-line)" stroke-width="10"/>
    <line x1="1086" y1="252" x2="1086" y2="640" stroke="var(--roof-line)" stroke-width="10"/>
  </svg>

  <div class="banner"></div>
  <div class="tool-mark" role="img" aria-label="Wrench emblem"></div>
  <div class="brand">HANDYMAN SERVICES<br>07700900461</div>

  <div class="roofer" role="img" aria-label="Figure of a worker carrying a ladder on the roof"></div>
  <div class="roof-label">repair roofs</div>

  <section class="intro">
    <h1>NO JOB TOO SMALL</h1>
    <p>we provide a good,and reliable service.<br>we do all aspects of home improvement,<br>also all garden services, and any repairs</p>
  </section>

  <div class="tile c1 r1"><span class="icon" role="img" aria-label="Security camera icon"></span><span class="label">cctv<br>installation</span></div>
  <div class="tile c2 r1 tall"><span class="icon" role="img" aria-label="Dripping tap icon"></span><span class="label">water features,<br>erect or repair<br>kitchens /<br>bathrooms</span></div>
  <div class="tile c3 r1 split">
    <div class="part"><span class="icon" role="img" aria-label="Garage icon"></span><span class="label">garages for<br>erecting / repairs</span></div>
    <div class="part"><span class="label">house /garage<br>clearances</span></div>
  </div>

  <div class="tile c1 r2 tall"><span class="icon" role="img" aria-label="Window icon"></span><span class="label">fit or repair<br>windows / doors,<br>lay patios</span></div>
  <div class="tile c2 r2"><span class="icon" role="img" aria-label="Wall lamp icon"></span><span class="label">decorate<br>interior /<br>external</span></div>
  <div class="tile c3 r2 tall"><span class="icon" role="img" aria-label="Drain pipe junction icon"></span><span class="label">lay drainage,<br>repair or erect<br>guttering and<br>soffits</span></div>

  <div class="tile c1 r3"><span class="icon" role="img" aria-label="Decking boards icon"></span><span class="label">decking,<br>lay driveways</span></div>
  <div class="tile c2 r3"><span class="icon" role="img" aria-label="Plastering trowel icon"></span><span class="label">plastering</span></div>
  <div class="tile c3 r3"><span class="icon" role="img" aria-label="Aerial icon"></span><span class="label">erect ariaels</span></div>

  <div class="tile c1 r4"><span class="icon" role="img" aria-label="Alarm signal icon"></span><span class="label">fit alarm systems</span></div>
  <div class="tile c2 r4"><span class="icon" role="img" aria-label="Fence icon"></span><span class="label">erect or repair<br>fencing</span></div>
  <div class="tile c3 r4"><span class="icon" role="img" aria-label="Garden shed icon"></span><span class="label">repair/erect<br>sheds</span></div>

  <svg class="badge" viewBox="0 0 250 250" aria-hidden="true">
    <polygon fill="var(--badge)" points="125,2 141,26 166,10 172,39 201,33 196,62 225,67 210,92 236,108 212,125 236,142 210,158 225,183 196,188 201,217 172,211 166,240 141,224 125,248 109,224 84,240 78,211 49,217 54,188 25,183 40,158 14,142 38,125 14,108 40,92 25,67 54,62 49,33 78,39 84,10 109,26"/>
  </svg>
  <div class="badge-text">special rates<br>for the elderly<hr>reducing the price<br>for anyone who<br>does a friend<br>reference</div>

  <div class="lawn" role="img" aria-label="Grass tufts along the ground"></div>
  <div class="mower" role="img" aria-label="Silhouette of a person pushing a lawn mower"></div>
  <div class="lawn-label">lay lawns</div>
  <div class="ground"><span class="ground-label">patio/driveway cleaning</span></div>
</main>
</body>
</html>
```